Fernvale Craft Works business card design- Fine Art sculpture business (Contract guaranteed)

This business card is for a fine art business. Though we don't have a website up and running yet it should be up soon. I would like the business card to be elegant and fairly simple with a picture of one of my sculptures on the front (you might need to photoshop out the background) as well as my basic contact info (my name,phone # and e-mail). On the back I'd like it to be pretty simple with just "Notes" and some blank lines for writing in info.

Target Market(s)

High end artwork buyers

Industry/Entity Type

Art Gallery

Contact Information for Business Card

Marlo Prewitt Phone: (555) 213-4098 E-mail: marlo@quillbrookmail.com Facebook: @fernvalecraftworks Instagram: fernvalecraftworks

Colors

Designer to choose colors to be used in the design.

Requirements
Must have
• *A picture of one of my sculptures*, my name, business name (Fernvale Craft Works), e-mail, phone #, and a notes section on the back.
• Fernvale Craft Works
• Marlo Prewitt
• (555)213-4098
• marlo@quillbrookmail.com
• Facebook: @fernvalecraftworks
• Instagram: fernvalecraftworks
Nice to have
• It'd be nice if you can crop out the background in the sculpture pictures, which ever one you end up using.

```html
<!DOCTYPE html>
<html lang="en">
<head>
<meta charset="utf-8">
<title>Fernvale Craft Works – Business Card</title>
<link rel="stylesheet" href="https://fonts.googleapis.com/css2?family=Josefin+Sans:wght@100;300&family=Arimo:wght@400&display=swap">
<style>
  :root {
    --backdrop: #b5b5b5;
    --card: #ffffff;
    --ink: #1f1030;
    --rule: #6b6a8c;
    --facet-light: #ece3f4;
    --facet-deep: #d3c2e6;
    --amethyst-dark: #2a1046;
    --amethyst: #6a3fb0;
    --amethyst-light: #a77fe0;
    --plinth: #5d6664;
  }
  * { margin: 0; padding: 0; box-sizing: border-box; }
  html, body {
    width: 1030px; height: 1200px; overflow: hidden;
    background: var(--backdrop);
  }
  .card {
    position: absolute;
    background: var(--card);
    overflow: hidden;
  }
  .card--front { left: 78px; top: 63px; width: 869px; height: 496px; }
  .card--back  { left: 81px; top: 630px; width: 863px; height: 493px; }

  .facet-field { position: absolute; left: 0; top: 0; }

  .sculpture-photo {
    position: absolute; left: 611px; top: 25px; width: 240px; height: 468px;
    background: radial-gradient(ellipse at 55% 40%, var(--amethyst-light) 0%, var(--amethyst) 40%, var(--amethyst-dark) 75%, transparent 76%),
                linear-gradient(to top, var(--plinth) 0 14%, transparent 14%);
    border-radius: 40% 40% 12% 12% / 30% 30% 8% 8%;
  }

  .brand-name {
    position: absolute; right: 264px; top: 214px;
    font-family: "Josefin Sans", sans-serif; font-weight: 100;
    color: var(--ink); text-align: right; line-height: 1;
  }
  .brand-name__main { display: block; font-size: 52px; letter-spacing: 1px; }
  .brand-name__sub  { display: block; font-size: 34px; margin-top: 6px; letter-spacing: 1px; }

  .contact {
    position: absolute; font-family: "Arimo", Arial, sans-serif;
    font-size: 25px; color: var(--ink); white-space: nowrap;
  }
  .contact--name  { left: 114px; top: 420px; }
  .contact--phone { left: 329px; top: 420px; }
  .contact--email { left: 100px; top: 454px; width: 520px; text-align: center; font-size: 24px; }

  .notes-title {
    position: absolute; left: 509px; top: 27px;
    font-family: "Josefin Sans", sans-serif; font-weight: 100;
    font-size: 48px; color: var(--ink); line-height: 1;
  }
  .note-line {
    position: absolute; height: 1px; background: var(--rule);
  }
  .note-line--short { left: 338px; width: 489px; }
  .note-line--long  { left: 231px; width: 596px; }
</style>
</head>
<body>
  <section class="card card--front">
    <svg class="facet-field" width="340" height="496" role="img" aria-label="Geometric faceted line pattern in purple and blue">
      <defs>
        <linearGradient id="facetFront" x1="0" y1="0" x2="1" y2="1">
          <stop offset="0" stop-color="var(--facet-deep)"/>
          <stop offset="1" stop-color="var(--facet-light)"/>
        </linearGradient>
      </defs>
      <polygon points="0,0 334,0 314,25 294,163 210,163 158,215 136,289 34,359 82,425 138,496 0,496" fill="url(#facetFront)"/>
    </svg>

    <h1 class="brand-name">
      <span class="brand-name__main">FERNVALE CRAFT</span>
      <span class="brand-name__sub">WORKS</span>
    </h1>

    <div class="sculpture-photo" role="img" aria-label="Photo of an amethyst crystal sculpture on a granite base"></div>

    <p class="contact contact--name">Marlo Prewitt</p>
    <p class="contact contact--phone">Phone: (555) 213-4098</p>
    <p class="contact contact--email">E-mail: marlo.prewitt4@quillbrookmail.com</p>
  </section>

  <section class="card card--back">
    <svg class="facet-field" width="350" height="493" role="img" aria-label="Geometric faceted line pattern in purple and blue">
      <defs>
        <linearGradient id="facetBack" x1="0" y1="0" x2="1" y2="1">
          <stop offset="0" stop-color="var(--facet-deep)"/>
          <stop offset="1" stop-color="var(--facet-light)"/>
        </linearGradient>
      </defs>
      <polygon points="0,0 344,0 323,26 306,165 223,165 171,215 147,290 46,360 87,418 149,493 0,493" fill="url(#facetBack)"/>
    </svg>

    <h2 class="notes-title">NOTES</h2>

    <div class="note-line note-line--short" style="top:95px"></div>
    <div class="note-line note-line--short" style="top:134px"></div>
    <div class="note-line note-line--short" style="top:173px"></div>
    <div class="note-line note-line--long" style="top:213px"></div>
    <div class="note-line note-line--long" style="top:255px"></div>
    <div class="note-line note-line--long" style="top:298px"></div>
    <div class="note-line note-line--long" style="top:338px"></div>
    <div class="note-line note-line--long" style="top:379px"></div>
    <div class="note-line note-line--long" style="top:419px"></div>
    <div class="note-line note-line--long" style="top:459px"></div>
  </section>
</body>
</html>
```